Business Card Design

I need a business card for my tutoring service. Key elements on front are its contact details and visual appeal with these three points: All aspects of literacy and numeracy, 'Bright Steps Program Plus' provider and Prep-readiness sessions
Updates

contact me by email on danafor7@quillmail.net as I'm having issues with other address at times. Thanks

:) 

Target Market(s)

People with children

Industry/Entity Type

Tutoring

Contact Information for Business Card

Dana Forsythe Educational Consultant
12 Tamarind Rise
Burpengary 4505
0471 388 912

Requirements
Nice to have
• Something related to education. On the back of the card, my business name and phone number again, along with: spelling, reading, writing, comprehension, oral language, listening skills

```html
<!DOCTYPE html>
<html lang="en">
<head>
<meta charset="utf-8">
<title>Dana's Tutoring Service – Business Card</title>
<link href="https://fonts.googleapis.com/css2?family=Amatic+SC:wght@700&family=Open+Sans:ital,wght@0,600;0,700;1,400&family=Varela+Round&display=swap" rel="stylesheet">
<style>
  :root {
    --page: #ffffff;
    --board: #272d2b;
    --board-light: #333a38;
    --chalk: #f2f2ee;
    --pink: #d1397a;
    --teal: #3ba6b7;
    --lime: #c9d94b;
    --ink: #111111;
    --grey: #8a8a8a;
    --outline: #333333;
  }
  * { margin: 0; padding: 0; box-sizing: border-box; }
  html, body { width: 1200px; height: 498px; overflow: hidden; background: var(--page); }
  .canvas { position: relative; width: 1200px; height: 498px; }

  /* Front */
  .card-front {
    position: absolute; left: 73px; top: 72px; width: 554px; height: 353px;
    background: radial-gradient(ellipse at 50% 40%, var(--board-light) 0%, var(--board) 70%);
    border-radius: 14px; overflow: hidden;
  }
  .front-title {
    position: absolute; left: 0; top: 30px; width: 554px; text-align: center;
    font-family: "Amatic SC", cursive; font-weight: 700; font-size: 54px;
    text-transform: uppercase; color: var(--teal); line-height: 1; letter-spacing: 1px;
  }

  .contact { position: absolute; left: 20px; top: 134px; width: 258px; text-align: center;
    font-family: "Open Sans", sans-serif; color: var(--chalk); }
  .contact .name { color: var(--pink); font-weight: 700; font-size: 21px; }
  .contact .role { font-style: italic; font-size: 18px; margin-top: 4px; }
  .contact .address { font-weight: 600; font-size: 15.5px; line-height: 25px; margin-top: 33px; }
  .contact .phone { font-weight: 700; font-size: 18px; margin-top: 12px; }

  .services-frame { position: absolute; left: 278px; top: 125px; }
  .services-line {
    position: absolute; left: 279px; width: 224px; text-align: center;
    font-family: "Amatic SC", cursive; font-weight: 700; font-size: 21px;
    text-transform: uppercase; line-height: 1;
  }
  .services-line.program { top: 132px; color: var(--teal); }
  .services-line.offer { color: var(--lime); }
  .services-line.offer-1 { top: 180px; }
  .services-line.offer-2 { top: 205px; }
  .services-line.offer-3 { top: 229px; }
  .services-line.prep { top: 282px; color: var(--lime); }
  .services-divider { position: absolute; left: 367px; top: 267px; width: 32px; height: 2px; background: var(--lime); }

  /* Back */
  .card-back { position: absolute; left: 700px; top: 136px; width: 460px; text-align: center; }
  .back-title { font-family: "Amatic SC", cursive; font-weight: 700; font-size: 48px;
    text-transform: uppercase; color: var(--ink); line-height: 1; letter-spacing: 1px; }
  .back-phone { font-family: "Varela Round", sans-serif; font-size: 29px;
    color: var(--grey); -webkit-text-stroke: 1.5px var(--outline); line-height: 1; margin-top: 2px; letter-spacing: 1px; }
  .skills { font-family: "Amatic SC", cursive; font-weight: 700; font-size: 28px;
    text-transform: uppercase; color: var(--ink); line-height: 50px; margin-top: 48px; letter-spacing: 0.5px; }
</style>
</head>
<body>
<div class="canvas">

  <section class="card-front">
    <h1 class="front-title">Dana's Tutoring Service</h1>

    <div class="contact">
      <p class="name">Dana Forsythe</p>
      <p class="role">Educational Consultant</p>
      <p class="address">12 Tamarind Rise<br>Wattlegrove North 4999</p>
      <p class="phone">0471 388 912</p>
    </div>

    <svg class="services-frame" width="246" height="196" viewBox="0 0 246 196">
      <rect x="2" y="2" width="241" height="190" fill="none" stroke="var(--chalk)" stroke-width="1.6" stroke-dasharray="6 2 2 2"/>
      <line x1="2" y1="37" x2="243" y2="37" stroke="var(--chalk)" stroke-width="1.6" stroke-dasharray="6 2 2 2"/>
      <rect x="6" y="40" width="233" height="148" fill="none" stroke="var(--chalk)" stroke-width="1.4" stroke-dasharray="5 2 2 2"/>
    </svg>
    <p class="services-line program">Bright Steps Program Plus</p>
    <p class="services-line offer offer-1">All aspects of literacy</p>
    <p class="services-line offer offer-2">&amp;</p>
    <p class="services-line offer offer-3">Numeracy provider</p>
    <span class="services-divider"></span>
    <p class="services-line prep">Prep-readiness sessions</p>
  </section>

  <section class="card-back">
    <h2 class="back-title">Dana's Tutoring Service</h2>
    <p class="back-phone">0471 388 912</p>
    <p class="skills">Spelling • Reading • Writing • Comprehension<br>Oral Language • Listening Skills</p>
  </section>

</div>
</body>
</html>
```